Business cards, letter head, stationery
trial lawyer
Bright & Fun-filled
Teodoro Villaseca
Trial Lawyer
2716 kelverham, suite 300
Corvandale Texas 77538
Tevmilux@quarnela.com
Need to include:
Offices in Marrowfield , Santo Velaro, and Quill Crossing Texas
Use winning logo

```html
<!DOCTYPE html>
<html lang="en">
<head>
<meta charset="utf-8">
<title>Teodoro Villaseca — Stationery Set</title>
<link rel="stylesheet" href="https://fonts.googleapis.com/css2?family=Cinzel:wght@700&family=Open+Sans:wght@400;600&display=swap">
<style>
  :root{
    --ink:#111111;
    --paper:#ffffff;
    --stage:#e9e9e7;
    --body:#4a4a4a;
    --muted:#8a8a8a;
    --footer-light:#d8d8d8;
    --mark-faint:rgba(0,0,0,0.06);
  }
  *{box-sizing:border-box;margin:0;padding:0}
  html,body{width:1200px;height:587px;overflow:hidden;background:var(--stage)}
  body{position:relative;font-family:"Open Sans",Arial,sans-serif;color:var(--body)}
  .sheet{position:absolute;background:var(--paper);overflow:hidden;box-shadow:0 1px 3px rgba(0,0,0,.18)}
  .swoosh{position:absolute;left:0;width:100%;display:block}
  .brand{position:absolute;display:flex;align-items:center;gap:5px;font-family:"Cinzel",Georgia,serif;font-weight:700;color:var(--ink);white-space:nowrap;letter-spacing:.04em}
  .brand-square{display:block;background:var(--ink)}
  .brand.on-dark{color:var(--paper)}
  .brand.on-dark .brand-square{background:var(--paper)}
  .faint-square{position:absolute;background:var(--mark-faint)}

  /* envelopes */
  .envelope-back{left:12px;top:12px;width:228px;height:118px}
  .envelope-front{left:12px;top:140px;width:228px;height:190px}
  .envelope-small{left:12px;top:342px;width:228px;height:150px}
  .env-address{position:absolute;font-size:5px;line-height:7px;color:var(--muted)}

  /* letterheads */
  .letterhead{top:12px;width:296px;height:559px}
  .letterhead.first{left:272px}
  .letterhead.second{left:572px}
  .letterhead .brand{left:50%;transform:translateX(-50%);top:18px;font-size:11px}
  .letterhead .brand-square{width:14px;height:14px}
  .letterhead .faint-square{left:88px;top:215px;width:120px;height:120px}
  .recipient,.salutation,.letter-body,.sign-off{position:absolute;left:24px;font-size:6.2px;line-height:8.6px}
  .recipient{top:58px}
  .salutation{top:104px}
  .letter-body{top:122px;width:250px}
  .letter-body p{margin-bottom:10px}
  .sign-off{top:470px}
  .letter-footer{position:absolute;left:0;bottom:8px;width:100%;text-align:center;font-size:4.6px;color:var(--muted);letter-spacing:.02em}
  .letter-footer.on-dark{color:var(--footer-light)}
  .letter-footer.raised{bottom:44px}

  /* business cards */
  .card{height:112px}
  .card-front{left:870px;top:262px;width:196px}
  .card-back{left:992px;top:330px;width:196px;background:var(--ink)}
  .card-front .brand{left:10px;top:12px;font-size:7.5px;gap:4px}
  .card-front .brand-square{width:10px;height:10px}
  .card-details{position:absolute;left:10px;top:30px;font-size:5.4px;line-height:7.6px;color:var(--body);white-space:nowrap}
  .card-details .card-name{font-weight:600;color:var(--ink);font-size:6.4px}
  .card-back .brand{left:50%;top:50%;transform:translate(-50%,-50%);font-size:9px}
  .card-back .brand-square{width:12px;height:12px}
</style>
</head>
<body>

<!-- Envelope flap side -->
<div class="sheet envelope-back">
  <svg class="swoosh" style="top:0" width="228" height="118" viewBox="0 0 228 118" aria-hidden="true">
    <path d="M0 0H228V34C170 70 70 78 0 52Z" fill="var(--ink)"/>
    <path d="M0 60C70 86 170 80 228 44" fill="none" stroke="var(--ink)" stroke-width="1.5"/>
  </svg>
  <div class="brand" style="left:106px;top:82px;font-size:0"><span class="brand-square" style="width:16px;height:16px"></span></div>
</div>

<!-- Envelope front -->
<div class="sheet envelope-front">
  <span class="faint-square" style="left:128px;top:50px;width:84px;height:84px"></span>
  <div class="brand" style="left:10px;top:12px;font-size:8px"><span class="brand-square" style="width:11px;height:11px"></span>Teodoro Villaseca</div>
  <div class="env-address" style="left:10px;top:32px">2716 kelverham, suite 300<br>Corvandale Texas 77538</div>
  <svg class="swoosh" style="bottom:0" width="228" height="60" viewBox="0 0 228 60" aria-hidden="true">
    <path d="M0 60V48C80 56 170 40 228 6V60Z" fill="var(--ink)"/>
  </svg>
</div>

<!-- Small envelope -->
<div class="sheet envelope-small">
  <div class="brand" style="left:10px;top:10px;font-size:7px"><span class="brand-square" style="width:10px;height:10px"></span>Teodoro Villaseca</div>
  <div class="env-address" style="left:10px;top:26px">2716 kelverham, suite 300<br>Corvandale Texas 77538</div>
  <div class="env-address" style="left:10px;bottom:8px">Marrowfield · Santo Velaro · Quill Crossing, Texas</div>
</div>

<!-- Letterhead one -->
<div class="sheet letterhead first">
  <span class="faint-square"></span>
  <div class="brand"><span class="brand-square"></span>Teodoro Villaseca</div>
  <div class="recipient">Someone Somebody<br>100 Long St<br>Harlow Bay, Westmere</div>
  <div class="salutation">Dear Someone Somebody,</div>
  <div class="letter-body">
    <p>Lorem ipsum dolor sit amet, consectetuer adipiscing elit, sed diam nonummy nibh euismod tincidunt ut laoreet dolore magna aliquam erat volutpat. Ut wisi enim ad minim veniam, quis nostrud exerci tation ullamcorper suscipit lobortis nisl ut aliquip ex ea commodo consequat.</p>
    <p>Lorem ipsum dolor sit amet, consectetuer adipiscing elit, sed diam nonummy nibh euismod tincidunt ut laoreet dolore magna aliquam erat volutpat. Ut wisi enim ad minim veniam, quis nostrud exerci tation ullamcorper suscipit lobortis nisl ut aliquip ex ea commodo consequat.</p>
    <p>Lorem ipsum dolor sit amet, consectetuer adipiscing elit, sed diam nonummy nibh euismod tincidunt ut laoreet dolore magna aliquam erat volutpat. Ut wisi enim ad minim veniam, quis nostrud exerci tation ullamcorper suscipit lobortis nisl ut aliquip ex ea commodo consequat.</p>
    <p>Lorem ipsum dolor sit amet, consectetuer adipiscing elit, sed diam nonummy nibh euismod tincidunt ut laoreet dolore magna aliquam erat volutpat. Ut wisi enim ad minim veniam, quis nostrud exerci tation ullamcorper suscipit lobortis nisl ut aliquip ex ea commodo consequat.</p>
    <p>Lorem ipsum dolor sit amet, consectetuer adipiscing elit, sed diam nonummy nibh euismod tincidunt ut laoreet dolore magna aliquam erat volutpat. Ut wisi enim ad minim veniam, quis nostrud exerci tation ullamcorper suscipit lobortis nisl ut aliquip ex ea commodo consequat.</p>
  </div>
  <div class="sign-off">Yours Sincerely<br><br>Teodoro Villaseca</div>
  <svg class="swoosh" style="bottom:0" width="296" height="60" viewBox="0 0 296 60" aria-hidden="true">
    <path d="M0 60V30C90 52 200 46 296 10V60Z" fill="var(--ink)"/>
    <path d="M0 22C90 44 200 38 296 2" fill="none" stroke="var(--ink)" stroke-width="1"/>
  </svg>
  <div class="letter-footer on-dark">2716 kelverham, suite 300 · Corvandale Texas 77538 · Tevmilux@quarnela.com</div>
</div>

<!-- Letterhead two -->
<div class="sheet letterhead second">
  <span class="faint-square"></span>
  <div class="brand"><span class="brand-square"></span>Teodoro Villaseca</div>
  <div class="recipient">Someone Somebody<br>100 Long St<br>Harlow Bay, Westmere</div>
  <div class="salutation">Dear Someone Somebody,</div>
  <div class="letter-body">
    <p>Lorem ipsum dolor sit amet, consectetuer adipiscing elit, sed diam nonummy nibh euismod tincidunt ut laoreet dolore magna aliquam erat volutpat. Ut wisi enim ad minim veniam, quis nostrud exerci tation ullamcorper suscipit lobortis nisl ut aliquip ex ea commodo consequat.</p>
    <p>Lorem ipsum dolor sit amet, consectetuer adipiscing elit, sed diam nonummy nibh euismod tincidunt ut laoreet dolore magna aliquam erat volutpat. Ut wisi enim ad minim veniam, quis nostrud exerci tation ullamcorper suscipit lobortis nisl ut aliquip ex ea commodo consequat.</p>
    <p>Lorem ipsum dolor sit amet, consectetuer adipiscing elit, sed diam nonummy nibh euismod tincidunt ut laoreet dolore magna aliquam erat volutpat. Ut wisi enim ad minim veniam, quis nostrud exerci tation ullamcorper suscipit lobortis nisl ut aliquip ex ea commodo consequat.</p>
    <p>Lorem ipsum dolor sit amet, consectetuer adipiscing elit, sed diam nonummy nibh euismod tincidunt ut laoreet dolore magna aliquam erat volutpat. Ut wisi enim ad minim veniam, quis nostrud exerci tation ullamcorper suscipit lobortis nisl ut aliquip ex ea commodo consequat.</p>
    <p>Lorem ipsum dolor sit amet, consectetuer adipiscing elit, sed diam nonummy nibh euismod tincidunt ut laoreet dolore magna aliquam erat volutpat. Ut wisi enim ad minim veniam, quis nostrud exerci tation ullamcorper suscipit lobortis nisl ut aliquip ex ea commodo consequat.</p>
  </div>
  <div class="sign-off">Yours Sincerely<br><br>Teodoro Villaseca</div>
  <svg class="swoosh" style="bottom:0" width="296" height="40" viewBox="0 0 296 40" aria-hidden="true">
    <path d="M0 40V30C100 40 210 30 296 4V40Z" fill="var(--ink)"/>
  </svg>
  <div class="letter-footer raised">Offices in Marrowfield · Santo Velaro · Quill Crossing, Texas</div>
</div>

<!-- Business card, front -->
<div class="sheet card card-front">
  <div class="brand"><span class="brand-square"></span>Teodoro Villaseca</div>
  <div class="card-details">
    <span class="card-name">Teodoro Villaseca</span><br>
    Trial Lawyer<br>
    2716 kelverham, suite 300<br>
    Corvandale Texas 77538<br>
    Tevmilux@quarnela.com
  </div>
  <svg class="swoosh" style="bottom:0" width="196" height="30" viewBox="0 0 196 30" aria-hidden="true">
    <path d="M0 30V22C70 30 140 22 196 2V30Z" fill="var(--ink)"/>
  </svg>
</div>

<!-- Business card, back -->
<div class="sheet card card-back">
  <div class="brand on-dark"><span class="brand-square"></span>Teodoro Villaseca</div>
</div>

</body>
</html>
```